Professional Business Card - Sparkline Nine
Wireless Communications
Professional Business Card - Sparkline Nine - Telecommunications
Professional
Mark Tolson
Technology Consultant
N/A
mark@tolspar.com
www.tolspar.com
We need this back in a Illustrator format in order to make revised copies. Feel free to bleed off of the page.
Digital Communication Devices Bramblecrest Fleet Dispatch Network We Improve Cellphone Coverage P25 - Public Safety Equipment Dispatch Consoles Digital Radio Rentals

```html
<!DOCTYPE html>
<html lang="en">
<head>
<meta charset="utf-8">
<title>Sparkline Nine – Business Card</title>
<link rel="stylesheet" href="https://fonts.googleapis.com/css2?family=Roboto:wght@400;700&display=swap">
<style>
  :root {
    --backdrop: #eceef1;
    --card: #ffffff;
    --ink: #1c1c1e;
    --ink-soft: #4a4a4f;
    --brand-red: #d8201f;
    --rule: #9a9aa0;
    --swoosh: #121212;
  }
  * { margin: 0; padding: 0; box-sizing: border-box; }
  html, body {
    width: 1200px;
    height: 799px;
    overflow: hidden;
    background: var(--backdrop);
    font-family: "Roboto", Arial, sans-serif;
  }
  .canvas {
    position: relative;
    width: 1200px;
    height: 799px;
  }
  .business-card {
    position: absolute;
    left: 100px;
    top: 114px;
    width: 1000px;
    height: 571px;
    background: var(--card);
    overflow: hidden;
    box-shadow: 0 10px 30px rgba(0, 0, 0, 0.12);
  }
  .brand {
    position: absolute;
    left: 70px;
    top: 170px;
    display: flex;
    align-items: center;
    gap: 18px;
  }
  .brand-dot {
    width: 34px;
    height: 34px;
    border-radius: 50%;
    background: var(--brand-red);
  }
  .brand-name {
    font-size: 46px;
    font-weight: 700;
    color: var(--ink);
    letter-spacing: 0.5px;
  }
  .divider {
    position: absolute;
    left: 510px;
    top: 80px;
    width: 2px;
    height: 250px;
    background: var(--rule);
  }
  .contact {
    position: absolute;
    left: 550px;
    top: 92px;
    color: var(--ink-soft);
  }
  .contact-name {
    font-size: 44px;
    font-weight: 700;
    color: var(--brand-red);
    line-height: 1.1;
  }
  .contact-title {
    font-size: 20px;
    color: var(--ink);
    margin-top: 4px;
    margin-bottom: 32px;
  }
  .contact-list {
    list-style: none;
    font-size: 19px;
    line-height: 1.55;
  }
  .contact-list .label { color: var(--ink); }
  .card-waves {
    position: absolute;
    left: 0;
    bottom: 0;
    width: 1000px;
    height: 200px;
  }
  .wave-red { fill: var(--brand-red); }
  .wave-black { fill: var(--swoosh); }
</style>
</head>
<body>
<main class="canvas">
  <article class="business-card">
    <div class="brand">
      <span class="brand-dot"></span>
      <span class="brand-name">Sparkline Nine</span>
    </div>

    <div class="divider"></div>

    <section class="contact">
      <h1 class="contact-name">Mark Tolson</h1>
      <p class="contact-title">Technology Consultant</p>
      <ul class="contact-list">
        <li><span class="label">Phone:</span> 555-210-4400</li>
        <li><span class="label">Cell:</span> 555-364-0170</li>
        <li><span class="label">Email Add:</span> mark@tolspar.com</li>
        <li><span class="label">Website:</span> www.tolspar.com</li>
      </ul>
    </section>

    <svg class="card-waves" viewBox="0 0 1000 200" preserveAspectRatio="none" aria-hidden="true">
      <path class="wave-black" d="M0 118 C 220 70, 520 60, 1000 92 L 1000 104 C 560 78, 260 96, 0 126 Z"/>
      <path class="wave-red" d="M0 150 C 250 100, 560 96, 1000 110 L 1000 200 L 0 200 Z"/>
    </svg>
  </article>
</main>
</body>
</html>
```